Veterinary Hospital Brochure - 2 Drafts - 1 Normal and 1 Fun.

Meadowbrook Pet Hospital needs a brochure to promote our veterinary hospital. These will be delivered to local mailboxes. I would like to see atleast 2 submissions from each designer.
One submission conservative and A4 folded DL and another submission more radical and interesting with innovative folding or crazy concepts. Maybe the brochure could be designed to fold into a dog house ?
I want at least one version to be VERY SIMPLE AND INTIMATE.
Our existing website is here: http://furlane.example/ and our new website will look like this: http://trial4.pagemint.example/#home
Please use colors and images from the new website, and information from the old website. The heading font used in the new site is Qorvatype - Otter Tilt Sketchline
I want the brochure to be simple and engaging on first view, and then provide the opportunity to find more information if desired. The brochure needs to be captivating on the outside so people don't throw it away immediately.

We will soon need letterhead, flags, pens, business cards, signs and vouchers so there is the opportunity for more work for the successful designer.

Target Market(s)

Women 25 to 44

Industry/Entity Type

Veterinary

Contact Information for Business Card

Meadowbrook Pet Hospital
14 Marlow Crescent
Tamsworth Vale
NSW 2417
Phone: 02 61938205
Emergency: 0417360592
Fax: 02 83159462
www.meadowbrookvets.example
contact@meadowbrookvets.example

Font styles to use
Script

Requirements
Must have
• Colors from the new website: http://meadowbrookvets.example/ and new logo.
• Information from the old website: http://furlane.example/
• 2 drafts - A normal A4 folded DL flyer and an interesting crazy design.
Nice to have
• VERY SIMPLE
• Subdued
• Intimate
Should not have
• Intense colours
• Red

```html
<!DOCTYPE html>
<html lang="en">
<head>
<meta charset="utf-8">
<title>Meadowbrook Pet Hospital – Pet Care Basics Brochure</title>
<link rel="stylesheet" href="https://fonts.googleapis.com/css2?family=Lato:wght@400;700&display=swap">
<style>
  :root {
    --orange: #f6893f;
    --green: #8cc63f;
    --green-dark: #6fa52a;
    --white: #ffffff;
    --cream: #fbf3ea;
    --brown: #6b4a32;
    --backdrop: #e4e6e8;
  }
  * { box-sizing: border-box; margin: 0; padding: 0; }
  html, body {
    width: 1200px;
    height: 1059px;
    overflow: hidden;
    background: var(--backdrop);
    font-family: "Lato", Arial, sans-serif;
  }
  .brochure {
    position: absolute;
    left: 40px;
    top: 80px;
    width: 1120px;
    height: 900px;
    box-shadow: 0 10px 30px rgba(0,0,0,0.18);
    overflow: hidden;
  }
  .brochure-shapes {
    position: absolute;
    inset: 0;
    width: 1120px;
    height: 900px;
  }
  .care-panel {
    position: absolute;
    left: 40px;
    top: 44px;
    width: 340px;
    color: var(--white);
  }
  .care-title {
    font-size: 40px;
    font-weight: 400;
    letter-spacing: 0.3px;
    margin-bottom: 22px;
  }
  .care-list { list-style: none; }
  .care-list li {
    position: relative;
    padding-left: 22px;
    font-size: 19px;
    line-height: 1.2;
    margin-bottom: 15px;
  }
  .care-list li::before {
    content: "";
    position: absolute;
    left: 0;
    top: 5px;
    width: 10px;
    height: 12px;
    background: linear-gradient(135deg, var(--green) 50%, var(--green-dark) 50%);
  }
  .vet-note {
    position: absolute;
    left: 62px;
    top: 585px;
    width: 232px;
    height: 232px;
    border-radius: 50%;
    background: var(--green);
    color: var(--white);
    display: flex;
    align-items: center;
    justify-content: center;
    text-align: center;
    padding: 0 22px;
    font-size: 17.5px;
    line-height: 1.25;
  }
  .register {
    position: absolute;
    left: 0;
    width: 370px;
    top: 812px;
    text-align: center;
    color: var(--white);
  }
  .register-title { font-size: 25px; font-weight: 700; }
  .register-phone { font-size: 18px; font-weight: 700; margin-top: 6px; }
  .class-blurb {
    position: absolute;
    left: 410px;
    top: 430px;
    width: 330px;
    color: var(--cream);
    font-size: 17px;
    line-height: 1.4;
  }
  .hospital-name {
    position: absolute;
    left: 792px;
    top: 395px;
    width: 176px;
    text-align: center;
    color: var(--brown);
    font-size: 19px;
    font-weight: 700;
    line-height: 1.2;
  }
</style>
</head>
<body>
  <main class="brochure">
    <svg class="brochure-shapes" viewBox="0 0 1120 900" xmlns="http://www.w3.org/2000/svg">
      <defs>
        <linearGradient id="puppy-photo-tone" x1="0" y1="0" x2="1" y2="1">
          <stop offset="0" stop-color="#e9dccb"/>
          <stop offset="0.5" stop-color="#c9a27a"/>
          <stop offset="1" stop-color="#a9754a"/>
        </linearGradient>
        <linearGradient id="cat-photo-tone" x1="0" y1="0" x2="1" y2="1">
          <stop offset="0" stop-color="#d9cbbb"/>
          <stop offset="0.55" stop-color="#9c8674"/>
          <stop offset="1" stop-color="#5e4a3d"/>
        </linearGradient>
      </defs>

      <rect class="base-orange" width="1120" height="900" fill="var(--orange)"/>

      <path class="wave-band" fill="var(--white)"
        d="M0 600 C 150 540, 290 660, 450 630
           C 610 600, 760 560, 880 520
           C 970 490, 1050 455, 1120 430
           L1120 900 L720 900 L720 680
           C 560 690, 440 730, 300 720
           C 180 712, 80 660, 0 690 Z"/>

      <path class="puppy-photo" role="img" aria-label="Photo of a puppy giving a high five to a woman outdoors"
        fill="url(#puppy-photo-tone)"
        d="M400 0 L1120 0 L1120 300 C 1040 300, 980 390, 880 420 C 720 470, 540 440, 450 300 C 420 240, 405 120, 400 0 Z"/>
      <path class="puppy-photo-rim" fill="none" stroke="var(--green)" stroke-width="6"
        d="M400 0 C 405 120, 420 240, 450 300 C 540 440, 720 470, 880 420"/>

      <path class="cat-photo" role="img" aria-label="Photo of a tabby cat being stroked on a woman's lap"
        fill="url(#cat-photo-tone)"
        d="M400 900 C 400 780, 500 660, 680 640 C 860 620, 1020 640, 1120 660 L1120 900 Z"/>
      <path class="cat-photo-rim" fill="none" stroke="var(--green)" stroke-width="6"
        d="M400 900 C 400 780, 500 660, 680 640 C 860 620, 1020 640, 1120 660"/>

      <circle class="name-badge" cx="880" cy="420" r="88" fill="var(--white)" stroke="var(--green)" stroke-width="6"/>
    </svg>

    <section class="care-panel">
      <h1 class="care-title">Pet Care Basics</h1>
      <ul class="care-list">
        <li>Yearly Vaccination and Checkup.</li>
        <li>Microchipping.</li>
        <li>Premium Food.</li>
        <li>Heartworming.</li>
        <li>Socialisation.</li>
        <li>Intestinal Worming.</li>
        <li>Sterilisation.</li>
        <li>Flea Treatment.</li>
        <li>Dental Care.</li>
        <li>Environmental Enrichment.</li>
      </ul>
    </section>

    <p class="vet-note">We usually do these at vaccination. A Vet check is essential atleast once per year, twice a year for senior pets.</p>

    <div class="register">
      <p class="register-title">Register Today</p>
      <p class="register-phone">Phone 61938205</p>
    </div>

    <p class="class-blurb">The classes are so much fun.<br>You will learn heaps and your puppy will have a great time socialising.</p>

    <p class="hospital-name">Meadowbrook<br>Pet Hospital</p>
  </main>
</body>
</html>
```